Brindell Excavation and Landscaping

I need a double sided card thick with rounded edges. I want an identical card of one of your designs but with my name on it on one side. Othe side I want my name,number under owner operator and a list of what I do. , drainage,grading,trenching stump removal , postholes. Landscaping lawn renovations, and reconfigurations, small to large rip outs and installs,sod work and burms and swails for water run off and plantings the two pictures of cards is what I like

Reason: First time doing this not sure if two days was enough, no one was taking on project so trying to figure out why I posted a picture of what I want so should be relatively easy

Industry/Entity Type

Landscaping

Contact Information for Business Card

Name Ted Brindell
Harlow Ridge county Phone 860-555-0143

Font styles to use
Other font styles liked:
• It's on card I sent second one

Requirements
Must have
• Same colors and look of card at bottom
Nice to have
• All aspects of excavation and landscaping on back of card
• Will add web address at end

```html
<!DOCTYPE html>
<html lang="en">
<head>
<meta charset="utf-8">
<title>Brindell Excavation and Landscaping – Business Card</title>
<link href="https://fonts.googleapis.com/css2?family=Open+Sans:wght@400;600;700&display=swap" rel="stylesheet">
<style>
  :root {
    --page: #ecebe8;
    --card-dark: #1c1c1c;
    --card-light: #ffffff;
    --orange: #f26a21;
    --orange-soft: #f4804a;
    --ink: #2b2b2b;
    --ink-muted: #6f6f6f;
    --rule: #8a8a8a;
    --on-dark: #f2f2f2;
  }
  * { box-sizing: border-box; margin: 0; padding: 0; }
  html, body {
    width: 1200px; height: 800px; overflow: hidden;
    background: var(--page);
    font-family: "Open Sans", Arial, sans-serif;
  }
  .sheet {
    width: 1200px; height: 800px;
    display: flex; align-items: center; justify-content: center; gap: 50px;
  }
  .card {
    width: 540px; height: 309px;
    border-radius: 22px;
    position: relative; overflow: hidden;
    box-shadow: 0 10px 28px rgba(0,0,0,.18);
  }

  /* Services side */
  .card--services {
    background: var(--card-dark);
    color: var(--on-dark);
    display: flex; flex-direction: column; align-items: center;
    padding-top: 56px;
  }
  .brand { display: flex; align-items: center; gap: 10px; }
  .brand__mark { width: 14px; height: 14px; background: var(--orange); flex: none; }
  .brand__name {
    color: var(--orange); font-weight: 700; text-transform: uppercase;
    letter-spacing: .05em; line-height: 1.15;
  }
  .card--services .brand__name { font-size: 17px; text-align: left; }
  .services {
    list-style: none; margin-top: 34px; text-align: center;
    font-size: 12.5px; line-height: 1.75; text-transform: uppercase;
    letter-spacing: .02em;
  }

  /* Contact side */
  .card--contact { background: var(--card-light); color: var(--ink); }
  .card--contact .brand { position: absolute; right: 28px; top: 62px; }
  .card--contact .brand__name { font-size: 13px; width: 200px; }
  .holder {
    position: absolute; left: 34px; top: 64px;
    border-left: 5px solid var(--orange); padding-left: 10px;
  }
  .holder__name { font-size: 22px; font-weight: 700; line-height: 1.1; }
  .holder__first { color: var(--orange); }
  .holder__role { font-size: 14px; color: var(--orange); }
  .divider {
    position: absolute; left: 0; right: 0; top: 130px; height: 2px;
    background: linear-gradient(90deg, var(--rule) 0 55%, var(--orange) 55% 100%);
  }
  .contacts {
    position: absolute; left: 34px; top: 152px;
    list-style: none; font-size: 13px; color: var(--ink-muted);
  }
  .contacts li { display: flex; align-items: center; gap: 10px; height: 28px; }
  .contacts svg { width: 20px; height: 20px; flex: none; }
  .band {
    position: absolute; left: 0; right: 0; bottom: 0; height: 56px;
    background: linear-gradient(180deg, var(--orange-soft), var(--orange));
    display: flex; align-items: center; padding-left: 34px;
    color: #fff; font-size: 15px; letter-spacing: .02em;
  }
</style>
</head>
<body>
<main class="sheet">

  <section class="card card--services" aria-label="Card back: services">
    <div class="brand">
      <span class="brand__mark"></span>
      <span class="brand__name">Brindell<br>Excavation and Landscaping</span>
    </div>
    <ul class="services">
      <li>Drainage | Grading | Trenching | Stump Removal | Postholes</li>
      <li>Landscaping Lawn Renovations &amp; Reconfigurations</li>
      <li>Small to Large Rip Outs and Installs | Sod Work | Planting</li>
      <li>Burms and Swails for Water Run Off</li>
    </ul>
  </section>

  <section class="card card--contact" aria-label="Card front: contact">
    <div class="brand">
      <span class="brand__mark"></span>
      <span class="brand__name">Brindell Excavation and Landscaping</span>
    </div>
    <div class="holder">
      <p class="holder__name"><span class="holder__first">Ted</span> Brindell</p>
      <p class="holder__role">Owner</p>
    </div>
    <div class="divider"></div>
    <ul class="contacts">
      <li>
        <svg viewBox="0 0 20 20" aria-hidden="true"><circle cx="10" cy="10" r="9" fill="none" stroke="#bbb"/><path d="M10 5a3 3 0 0 0-3 3c0 2.3 3 6 3 6s3-3.7 3-6a3 3 0 0 0-3-3z" fill="#f26a21"/><circle cx="10" cy="8" r="1" fill="#fff"/></svg>
        Harlow Ridge county
      </li>
      <li>
        <svg viewBox="0 0 20 20" aria-hidden="true"><circle cx="10" cy="10" r="9" fill="none" stroke="#bbb"/><path d="M6.5 6h2l1 2.2-1.2 1a6 6 0 0 0 2.5 2.5l1-1.2 2.2 1v2a1 1 0 0 1-1 1A7.5 7.5 0 0 1 5.5 7a1 1 0 0 1 1-1z" fill="#f26a21"/></svg>
        860-555-0143
      </li>
      <li>
        <svg viewBox="0 0 20 20" aria-hidden="true"><circle cx="10" cy="10" r="9" fill="none" stroke="#bbb"/><rect x="5.5" y="6.5" width="9" height="7" rx="1" fill="#f26a21"/><path d="M5.8 7l4.2 3.3L14.2 7" fill="none" stroke="#fff" stroke-width="1"/></svg>
        youremail@xyz.com
      </li>
    </ul>
    <div class="band">www.yourwebsite.com</div>
  </section>

</main>
</body>
</html>
```